Law Firm Website

I currently have a temporary site that I created myself at www.mcorveyfirm.net (hosted by 9tree). I am generally happy with the content.

My permanent website just has basic information right now: www.mcorveyfirm.com (hosted by lumenrack). I want to take the general content from the temporary website and have a more professional looking website on the permanent website. I want it in Wordpress format. I want a link to my blog: www.crookedpath.com. I want it to work on pads and smart phones. My number and e-mail address should be available on every page. The idea is to feature the potential client more than the lawyer.
Updates

Several of the designs are good. I would like the front page to have my number and address at the top (and at the top of every page) and to identify my law firm as "Law Office of Gerald T. Corvey". No need to include "mcorveyfirm" as that is just the web address. I like showing the most recent blog posts on the front page. I don't need video. No need to emphasize office hours or map location on the front page (that could be under a contact button). My picture should be somewhere. I would like an image from Boston on the front page if we can find one that is not copyright protected. No images of gavels or scales of justice. See some of the sample websites I listed in previous messages. Thanks!

Industry/Entity Type

Law Firm

```html
<!DOCTYPE html>
<html lang="en">
<head>
<meta charset="utf-8">
<title>Law Office of Gerald T. Corvey</title>
<link rel="stylesheet" href="https://fonts.googleapis.com/css2?family=Poiret+One&family=Oswald:wght@500&family=Open+Sans:wght@400;600;700&display=swap">
<style>
  :root {
    --navy: #0b2f6e;
    --navy-deep: #0a1f48;
    --ink: #1a1a1a;
    --muted: #555;
    --paper: #ebe8e2;
    --welcome: #dcdcdc;
    --footer: #1b2236;
    --bar: #0c0c0c;
    --white: #fff;
    --link-yellow: #f2d94a;
  }
  * { box-sizing: border-box; margin: 0; padding: 0; }
  html, body { width: 810px; height: 1200px; overflow: hidden; background: var(--white); }
  body { font-family: "Open Sans", Arial, sans-serif; color: var(--ink); }
  .canvas { position: relative; width: 810px; height: 1200px; overflow: hidden; }
  .abs { position: absolute; }

  /* Header */
  .site-header { top: 0; left: 0; width: 810px; height: 85px; background: linear-gradient(#fff, #ececec); }
  .brand-name { left: 101px; top: 14px; font-family: "Poiret One", sans-serif; font-size: 34px; color: #333; letter-spacing: .5px; }
  .brand-sub { left: 103px; top: 54px; font-family: "Poiret One", sans-serif; font-size: 11px; color: #777; }
  .contact { left: 578px; top: 10px; font-size: 9.5px; line-height: 12px; color: #222; }
  .contact-row { display: flex; gap: 4px; align-items: flex-start; margin-bottom: 5px; }
  .contact-row svg { flex: none; margin-top: 1px; }

  /* Nav */
  .main-nav { top: 85px; left: 0; width: 810px; height: 26px; background: var(--navy); border-bottom: 1px solid #3a5a9a; }
  .main-nav ul { list-style: none; display: flex; margin-left: 104px; height: 26px; align-items: center; }
  .main-nav li { color: var(--white); font-size: 8.6px; font-weight: 600; margin-right: 22px; white-space: nowrap; }

  /* Hero */
  .hero { top: 111px; left: 0; width: 810px; height: 217px;
    background: linear-gradient(180deg, #1c1c1c 0%, #3a3a3a 40%, #8c8c8c 62%, #2b2b2b 75%, #555 100%); }
  .slider-dots { top: 308px; left: 380px; display: flex; gap: 3px; }
  .slider-dots span { width: 10px; height: 10px; background: var(--white); }
  .slider-dots span.active { background: #b3222a; }
  .hero-tab { top: 326px; left: 101px; width: 607px; height: 6px; background: var(--navy-deep); }
  .hero-tab-pointer { top: 332px; left: 397px; }

  /* Welcome */
  .welcome { top: 332px; left: 0; width: 810px; height: 194px;
    background: radial-gradient(ellipse at 50% 40%, #f4f4f4 0%, var(--welcome) 70%); }
  .welcome-heading { right: 566px; top: 384px; text-align: right; font-family: "Oswald", sans-serif; font-weight: 500; font-size: 21px; line-height: 31px; color: var(--ink); letter-spacing: .3px; }
  .welcome-rule { left: 250px; top: 372px; width: 2px; height: 110px; background: #222; }
  .portrait-frame { left: 258px; top: 373px; width: 89px; height: 108px; background: var(--white); border: 1px solid #bbb; padding: 5px; }
  .portrait { width: 100%; height: 100%; background: linear-gradient(160deg, #6d6d6d, #2d2f35 60%, #1c2230); }
  .welcome-copy { left: 357px; top: 371px; width: 350px; }
  .welcome-copy h2 { font-size: 9.4px; font-weight: 700; line-height: 12px; color: var(--ink); margin-bottom: 5px; }
  .welcome-copy p { font-size: 8.3px; line-height: 11px; color: var(--muted); margin-bottom: 9px; }

  /* Practice areas */
  .practice { top: 526px; left: 0; width: 810px; height: 228px; background: var(--paper); }
  .practice-pointer { top: 526px; left: 398px; }
  .practice-title { left: 100px; top: 560px; font-size: 28px; font-weight: 700; color: #111; letter-spacing: .3px; }
  .practice-controls { left: 601px; top: 570px; width: 108px; height: 26px; background: var(--navy-deep); border-radius: 3px; display: flex; align-items: center; gap: 4px; padding-left: 10px; }
  .view-all-btn { border: 1px solid #cfd8ea; color: var(--white); font-size: 9px; padding: 2px 9px; }
  .arrow-btn { width: 14px; height: 14px; border-radius: 50%; background: #8a93a6; display: flex; align-items: center; justify-content: center; }
  .practice-cards { left: 101px; top: 604px; display: flex; gap: 5px; }
  .practice-card { position: relative; width: 148px; height: 101px; }
  .card-photo { width: 100%; height: 100%; }
  .card-caption { position: absolute; left: 0; bottom: 0; width: 100%; height: 33px; background: rgba(20,20,30,.55); display: flex; align-items: center; justify-content: center; text-align: center; color: var(--white); font-size: 10px; line-height: 11px; font-weight: 600; padding: 0 8px; }
  .card-caption::before { content: ""; position: absolute; inset: 3px 5px 5px 5px; border: 1px solid rgba(255,255,255,.45); border-bottom: none; }

  /* Blue section */
  .park { top: 754px; left: 0; width: 810px; height: 259px;
    background: linear-gradient(180deg, #26477f 0%, #2d4f8a 45%, #22406f 80%, #1a2f55 100%); }
  .park-pointer { top: 754px; left: 397px; }
  .review-panel { left: 101px; top: 773px; width: 264px; height: 205px; background: rgba(10,30,70,.75); }
  .review-title { left: 101px; top: 781px; width: 264px; text-align: center; color: var(--white); font-size: 13px; font-weight: 400; letter-spacing: .2px; }
  .field { left: 131px; width: 205px; background: var(--white); font-size: 7.5px; color: #333; padding: 6px 7px; }
  .submit-btn { left: 131px; top: 950px; width: 205px; height: 25px; background: #2f5190; border: 1px solid #6f87b8; color: var(--white); font-size: 10px; font-weight: 600; display: flex; align-items: center; justify-content: center; }
  .posts-title { left: 444px; top: 768px; color: var(--white); font-size: 13.5px; font-weight: 400; display: flex; align-items: center; gap: 4px; }
  .post { left: 444px; width: 264px; color: var(--white); font-size: 10px; line-height: 13px; }
  .read-more { position: absolute; right: 0; color: var(--link-yellow); font-size: 6.5px; display: flex; align-items: center; gap: 2px; }
  .posts-btn { left: 446px; top: 954px; width: 93px; height: 21px; background: #2f4e86; border: 1px solid #6f87b8; color: var(--white); font-size: 9px; display: flex; align-items: center; justify-content: center; gap: 4px; }

  /* Footer */
  .site-footer { top: 1013px; left: 0; width: 810px; height: 161px; background: radial-gradient(ellipse at 40% 50%, #2c3552 0%, var(--footer) 70%); }
  .footer-heading { color: #a8c2ea; font-size: 12px; font-weight: 400; line-height: 16px; }
  .sitemap { left: 101px; top: 1026px; }
  .sitemap ul { list-style: none; margin-top: 3px; }
  .sitemap li { color: var(--white); font-size: 8.4px; line-height: 15.4px; }
  .stories { left: 403px; top: 1026px; width: 320px; }
  .stories p { color: var(--white); font-size: 8.4px; line-height: 15.4px; margin-top: 3px; white-space: nowrap; }
  .stories p + p { margin-top: 15px; }
  .stories-btn { left: 403px; top: 1130px; width: 95px; height: 22px; background: #2f4e86; border: 1px solid #6f87b8; color: var(--white); font-size: 9px; display: flex; align-items: center; justify-content: center; gap: 4px; }
  .copyright { top: 1174px; left: 0; width: 810px; height: 26px; background: var(--bar); color: var(--white); font-size: 7px; display: flex; align-items: center; justify-content: center; }
</style>
</head>
<body>
<div class="canvas">

  <header class="site-header abs"></header>
  <div class="brand-name abs">Gerald T. Corvey</div>
  <div class="brand-sub abs">Law Office of Gerald T. Corvey</div>
  <div class="contact abs">
    <div class="contact-row">
      <svg width="9" height="12" viewBox="0 0 9 12"><path d="M4.5 0A4.5 4.5 0 0 0 0 4.5C0 8 4.5 12 4.5 12S9 8 9 4.5A4.5 4.5 0 0 0 4.5 0z" fill="#222"/><circle cx="4.5" cy="4.5" r="1.7" fill="#fff"/></svg>
      <span>118 Harlow St. 6th Floor<br>Boston, MA 02110</span>
    </div>
    <div class="contact-row" style="margin-bottom:1px">
      <svg width="9" height="9" viewBox="0 0 9 9"><path d="M0 3c0-2 9-2 9 0v1H6.5V3h-4v1H0z" fill="#222"/><rect x="1" y="5" width="7" height="4" rx="1" fill="#222"/></svg>
      <span>617 555-0142</span>
    </div>
    <div class="contact-row" style="margin-bottom:1px">
      <svg width="9" height="9" viewBox="0 0 9 9"><rect x="2" y="0" width="5" height="3" fill="#222"/><rect x="0" y="3" width="9" height="4" rx="1" fill="#222"/><rect x="2" y="6" width="5" height="3" fill="#222" stroke="#fff" stroke-width=".6"/></svg>
      <span>857 555-0187</span>
    </div>
    <div class="contact-row">
      <svg width="9" height="9" viewBox="0 0 9 9"><path d="M0 4l4.5-4 4.5 4v5H0z" fill="#222"/><path d="M1.5 4.5l3 2 3-2" stroke="#fff" stroke-width=".8" fill="none"/></svg>
      <span>gcorvey@mcorveyfirm.com</span>
    </div>
  </div>

  <nav class="main-nav abs">
    <ul>
      <li>Home</li><li>Why Hire Me?</li><li>Success Stories</li><li>Practice Areas</li>
      <li>Representative Clients</li><li>Services Provided</li><li>Contact Us</li><li>How To Find Us</li>
    </ul>
  </nav>

  <div class="hero abs" role="img" aria-label="Black and white night photograph of the Boston skyline across the river"></div>
  <div class="slider-dots abs"><span class="active"></span><span></span><span></span><span></span></div>
  <div class="hero-tab abs"></div>
  <svg class="hero-tab-pointer abs" width="16" height="8" viewBox="0 0 16 8"><path d="M0 0h16L8 8z" fill="#0a1f48"/></svg>

  <section class="welcome abs"></section>
  <h1 class="welcome-heading abs">WELCOME TO<br>LAW OFFICE OF<br>GERALD T. CORVEY</h1>
  <div class="welcome-rule abs"></div>
  <div class="portrait-frame abs"><div class="portrait" role="img" aria-label="Portrait photograph of the attorney in a dark suit"></div></div>
  <div class="welcome-copy abs">
    <h2>Protecting and Defending Your Business Against Competitors, Rogue Employees, Cheating Business Partners, Devious Contracting Parties, and Overzealous Government Agencies.</h2>
    <p>Your business is under constant attack.&nbsp; With more success, you become more of a target. Whether it's keeping you out of a lawsuit or defending one that you are already in (or prosecuting one when necessary), I'm here to help.</p>
    <p>Don't settle for lawyers who promise to work to solve your problems.&nbsp; I will work to prevent your problems in the first place.&nbsp; Learn more about litigation avoidance in my practice areas of law.</p>
  </div>

  <section class="practice abs"></section>
  <svg class="practice-pointer abs" width="14" height="10" viewBox="0 0 14 10"><path d="M0 0h14L7 10z" fill="#c9c9c9"/></svg>
  <h2 class="practice-title abs">Practics Area</h2>
  <div class="practice-controls abs">
    <span class="view-all-btn">View all</span>
    <span class="arrow-btn"><svg width="8" height="8" viewBox="0 0 8 8"><path d="M5 1L2 4l3 3" stroke="#fff" stroke-width="1.4" fill="none"/></svg></span>
    <span class="arrow-btn"><svg width="8" height="8" viewBox="0 0 8 8"><path d="M3 1l3 3-3 3" stroke="#fff" stroke-width="1.4" fill="none"/></svg></span>
  </div>
  <div class="practice-cards abs">
    <div class="practice-card">
      <div class="card-photo" role="img" aria-label="Photo of two businessmen shaking hands across a desk" style="background:linear-gradient(135deg,#e8e8e8,#7b7f88 55%,#3a3e48)"></div>
      <div class="card-caption">Employment Counseling and Litigation</div>
    </div>
    <div class="practice-card">
      <div class="card-photo" role="img" aria-label="Photo of colleagues in a business meeting" style="background:linear-gradient(135deg,#f1f1f1,#a7a29a 50%,#3c3d44)"></div>
      <div class="card-caption">Business Litigation</div>
    </div>
    <div class="practice-card">
      <div class="card-photo" role="img" aria-label="Photo of a hand holding documents in front of blue office towers" style="background:linear-gradient(135deg,#4a8fd6,#7fb2e6 45%,#2d5e9c)"></div>
      <div class="card-caption">Litigation Avoidance</div>
    </div>
    <div class="practice-card">
      <div class="card-photo" role="img" aria-label="Photo of business partners reviewing papers at a table" style="background:linear-gradient(135deg,#2a2c33,#6d6f76 50%,#d9d9d9)"></div>
      <div class="card-caption">Businesss Partner/ Shareholder Disputes.</div>
    </div>
  </div>

  <section class="park abs" role="img" aria-label="Blue tinted photograph of Boston Public Garden with an equestrian statue"></section>
  <svg class="park-pointer abs" width="16" height="10" viewBox="0 0 16 10"><path d="M0 0h16L8 10z" fill="#ebe8e2"/></svg>

  <div class="review-panel abs"></div>
  <h3 class="review-title abs">FREE CASE REVIEW</h3>
  <div class="field abs" style="top:802px;height:23px">Name</div>
  <div class="field abs" style="top:829px;height:23px">Phone</div>
  <div class="field abs" style="top:856px;height:23px">Email</div>
  <div class="field abs" style="top:883px;height:63px">Message</div>
  <div class="submit-btn abs">GET STARTED</div>

  <h3 class="posts-title abs">LATEST POSTS
    <svg width="175" height="12" viewBox="0 0 175 12"><path d="M0 2h175M0 6h175M0 10h175" stroke="#fff" stroke-width="1.2"/></svg>
  </h3>
  <div class="post abs" style="top:800px">You're Damned If You Don't Respond Appropriately to a Poor Rateline Review or Online Post.
    <span class="read-more" style="top:29px">Read more <svg width="10" height="5" viewBox="0 0 10 5"><path d="M0 2.5h9M7 .5l2 2-2 2" stroke="#fff" fill="none"/></svg></span></div>
  <div class="post abs" style="top:852px">You're Damned if You Don't Settle Meritorious Discrimination Cases
    <span class="read-more" style="top:26px">Read more <svg width="10" height="5" viewBox="0 0 10 5"><path d="M0 2.5h9M7 .5l2 2-2 2" stroke="#fff" fill="none"/></svg></span></div>
  <div class="post abs" style="top:902px">You May Be Damned if Your Drunk Employee Leaves the Company Party and Kills Someone in a Car Accident.
    <span class="read-more" style="top:26px">Read more <svg width="10" height="5" viewBox="0 0 10 5"><path d="M0 2.5h9M7 .5l2 2-2 2" stroke="#fff" fill="none"/></svg></span></div>
  <div class="posts-btn abs">View All <svg width="10" height="6" viewBox="0 0 10 6"><path d="M0 3h9M7 1l2 2-2 2" stroke="#fff" fill="none"/></svg></div>

  <footer class="site-footer abs"></footer>
  <div class="sitemap abs">
    <h4 class="footer-heading">SITE MAP</h4>
    <ul>
      <li>Home</li><li>Why Hire Me?</li><li>Success Stories</li><li>Practice Areas</li>
      <li>Representative Clients</li><li>Services Provided</li><li>Contact Us</li><li>How To Find Us</li>
    </ul>
  </div>
  <div class="stories abs">
    <h4 class="footer-heading">SUCCESS STORIES</h4>
    <p>Obtained Summary Judgment in favor of business client against multi-million<br>dollar claims of interference and conspiracy.</p>
    <p>&nbsp;Drafted executive employment and business contracts for a leading Hong<br>Kong electronic components manufacturer with a local Massachusetts office.</p>
  </div>
  <div class="stories-btn abs">View more <svg width="10" height="6" viewBox="0 0 10 6"><path d="M0 3h9M7 1l2 2-2 2" stroke="#fff" fill="none"/></svg></div>

  <div class="copyright abs">Copyright © 2014 Law office of Gerald T. Corvey | All right reserved.</div>
</div>
</body>
</html>
```